Company Letter head for formal business correspondence

Company needs a new facelift for stationary. Our letter head is impact as a professional service provider. We need to reflect professionalism in the Safety and Health environment. we work in the whole of the asia pacific region with our main base in Australia Queensland. We are a service company with consulting and operational focus. I have supplied our current logo. I have attached also our first letterhead that we didn't use, Wrong address on it also as we have moved since

Reason: Extension for design review due to modification with some designs currently and Xmas break issue.

Target Market(s)

New clients, government and global companys

Industry/Entity Type

Business

Font styles to use
Sans Serif

Requirements
Must have
• Logo, address, be in word format so l can use as a template and not just printed paper that l place in a printer.
• 41 Corlett Rd, Rockhampton, Queensland 4812.
• 1300718246 info@velminor.com
Nice to have
• a water mark in the back ground of the logo or partial log as one example supplied

```html
<!DOCTYPE html>
<html lang="en">
<head>
<meta charset="utf-8">
<title>Velminor Letterhead</title>
<link href="https://fonts.googleapis.com/css2?family=Roboto+Slab:wght@400;700&display=swap" rel="stylesheet">
<style>
  :root {
    --ink: #231f20;
    --text: #2b2b2b;
    --brand-red: #9b1b1f;
    --rule: #d4d4d4;
    --divider: #bdbdbd;
    --faint: #ececec;
    --paper: #ffffff;
  }
  html, body {
    margin: 0;
    padding: 0;
    width: 960px;
    height: 1200px;
    overflow: hidden;
    background: var(--paper);
  }
  .letterhead {
    position: relative;
    width: 960px;
    height: 1200px;
    background: var(--paper);
    font-family: "Roboto Slab", serif;
    color: var(--text);
  }
  .brand {
    position: absolute;
    left: 28px;
    top: 40px;
    display: flex;
    align-items: center;
    gap: 12px;
  }
  .brand-dot {
    width: 34px;
    height: 34px;
    border-radius: 50%;
    background: var(--brand-red);
  }
  .brand-name {
    font-weight: 700;
    font-size: 52px;
    line-height: 1;
    letter-spacing: -1px;
    color: var(--ink);
  }
  .corner-mark {
    position: absolute;
    right: 40px;
    top: 24px;
    width: 78px;
    height: 78px;
    border-radius: 50%;
    background: var(--faint);
  }
  .contact {
    position: absolute;
    left: 22px;
    top: 1108px;
    width: 680px;
    font-size: 19px;
  }
  .contact-row {
    display: flex;
    align-items: center;
    height: 30px;
  }
  .contact-row.address {
    padding-bottom: 10px;
    border-bottom: 2px solid var(--rule);
    width: 630px;
  }
  .contact-row.channels { margin-top: 12px; }
  .contact-item {
    display: flex;
    align-items: center;
    gap: 10px;
  }
  .contact-item svg { flex: none; }
  .divider {
    width: 1px;
    height: 22px;
    background: var(--divider);
    margin: 0 26px 0 28px;
  }
  .corner-curl {
    position: absolute;
    right: 0;
    bottom: 0;
    width: 280px;
    height: 232px;
  }
</style>
</head>
<body>
<main class="letterhead">
  <header class="brand">
    <span class="brand-dot"></span>
    <span class="brand-name">VELMINOR</span>
  </header>
  <div class="corner-mark" aria-hidden="true"></div>

  <footer class="contact">
    <div class="contact-row address">
      <span class="contact-item">
        <svg width="20" height="18" viewBox="0 0 20 18" aria-hidden="true"><path d="M10 0 L20 9 L17 9 L17 18 L12 18 L12 12 L8 12 L8 18 L3 18 L3 9 L0 9 Z" fill="var(--brand-red)"/></svg>
        41 Corlett Rd., Rockhampton, Queensland 4812
      </span>
    </div>
    <div class="contact-row channels">
      <span class="contact-item">
        <svg width="20" height="14" viewBox="0 0 20 14" aria-hidden="true"><rect width="20" height="14" fill="var(--brand-red)"/><path d="M0 0 L10 8 L20 0" stroke="#fff" stroke-width="1.6" fill="none"/></svg>
        info@velminor.com
      </span>
      <span class="divider"></span>
      <span class="contact-item">
        <svg width="22" height="22" viewBox="0 0 22 22" aria-hidden="true"><circle cx="11" cy="11" r="10" fill="none" stroke="var(--brand-red)" stroke-width="1.6"/><path d="M13 5 L10 6 C8 9 7 12 8 16 L11 17 L12 14 L10 13 C10 11 10.5 9.5 11.5 8 L13.5 8.5 Z" fill="var(--brand-red)"/></svg>
        1300 718 246
      </span>
      <span class="divider"></span>
      <span class="contact-item">
        <svg width="22" height="22" viewBox="0 0 22 22" aria-hidden="true"><circle cx="11" cy="11" r="10" fill="none" stroke="var(--brand-red)" stroke-width="1.6"/><path d="M13 5 L10 6 C8 9 7 12 8 16 L11 17 L12 14 L10 13 C10 11 10.5 9.5 11.5 8 L13.5 8.5 Z" fill="var(--brand-red)"/></svg>
        +61 0427 508 163
      </span>
    </div>
  </footer>

  <svg class="corner-curl" viewBox="0 0 315 268" preserveAspectRatio="none" aria-hidden="true">
    <path d="M0 268 C100 250 175 210 165 115 C230 112 290 70 315 0 L315 268 Z" fill="var(--brand-red)"/>
    <path d="M0 268 C130 258 240 215 315 110 L315 268 Z" fill="var(--ink)"/>
  </svg>
</main>
</body>
</html>
```